Bref créative
Stationary for Stonebrook Putting Institute
Driving range/Golf Academy
Simple
Pieter de Groenhout
Director of Golfschool
P.O. Box 48306
00452 Nairobi
pieter@stonebrookputt.co.ke
www.stonebrookputt.com
I am a TCA Professional from Holland and the logo off the TCA Holland should be incorporated at the business card. You can download it from the internet.
We have 2 other people who need business cards, Wilhelmina Drostraat CEO
Tom Wanjau Director
These two no TCA LOGO
Business card with black back ground, and for Pieter de Groenhout inclusive TCA Holland logo,
Letterhead the white background

```html
<!DOCTYPE html>
<html lang="en">
<head>
<meta charset="utf-8">
<title>Stonebrook Putting Institute — Business Cards</title>
<link href="https://fonts.googleapis.com/css2?family=Roboto:wght@400;500;700&display=swap" rel="stylesheet">
<style>
  :root{
    --stage:#e9e9ea;
    --card-black:#141414;
    --card-black-2:#232323;
    --brand-red:#d0121b;
    --brand-red-dark:#8c0a10;
    --steel-light:#d9dadc;
    --steel-dark:#7d7f83;
    --text-light:#f2f2f2;
    --text-muted:#b9b9b9;
  }
  *{margin:0;padding:0;box-sizing:border-box}
  html,body{width:1200px;height:737px;overflow:hidden}
  body{
    background:var(--stage);
    font-family:"Roboto",Arial,sans-serif;
    display:flex;align-items:center;justify-content:center;gap:60px;
  }
  .business-card{
    position:relative;width:525px;height:300px;border-radius:18px;overflow:hidden;
    background:linear-gradient(150deg,var(--card-black-2) 0%,var(--card-black) 60%);
    box-shadow:0 10px 28px rgba(0,0,0,.28);
  }
  .card-swoosh{position:absolute;inset:0;width:100%;height:100%}
  .wordmark{color:var(--text-light);font-weight:700;font-size:30px;letter-spacing:.5px;line-height:1;white-space:nowrap}
  .front .wordmark{position:absolute;left:34px;top:42px}
  .holder{position:absolute;right:34px;top:42px;text-align:right}
  .holder-name{color:var(--brand-red);font-weight:700;font-size:16px;line-height:1.2}
  .holder-role{color:var(--text-light);font-size:12px;margin-top:4px;letter-spacing:.3px}
  .contact{position:absolute;left:34px;top:150px;color:var(--text-muted);font-size:11.5px;line-height:1.65}
  .contact .web{color:var(--text-light);font-weight:500}
  .partner-badge{position:absolute;right:38px;bottom:34px;width:54px;height:54px;border-radius:50%;
    background:#fff;border:4px solid var(--brand-red)}
  .back .wordmark{position:absolute;left:50%;top:46%;transform:translate(-50%,-50%);font-size:40px}
</style>
</head>
<body>

<article class="business-card front" aria-label="Business card front">
  <svg class="card-swoosh" viewBox="0 0 525 300" preserveAspectRatio="none" aria-hidden="true">
    <defs>
      <linearGradient id="steelFront" x1="0" y1="0" x2="1" y2="1">
        <stop offset="0" stop-color="var(--steel-light)"/>
        <stop offset="1" stop-color="var(--steel-dark)"/>
      </linearGradient>
      <linearGradient id="redFront" x1="0" y1="0" x2="1" y2="0">
        <stop offset="0" stop-color="var(--brand-red-dark)"/>
        <stop offset="1" stop-color="var(--brand-red)"/>
      </linearGradient>
    </defs>
    <path d="M250 300 C330 250 400 190 525 160 L525 300 Z" fill="url(#steelFront)"/>
    <path d="M230 300 C320 240 400 175 525 145 L525 162 C410 190 340 248 262 300 Z" fill="url(#redFront)"/>
  </svg>

  <p class="wordmark">Stonebrook</p>

  <div class="holder">
    <p class="holder-name">Pieter de Groenhout</p>
    <p class="holder-role">Director of Golfschool</p>
  </div>

  <div class="contact">
    <p>P.O. Box 48306</p>
    <p>00452 Nairobi</p>
    <p>Tel: +254 20 555 0184</p>
    <p>Mob: +254 722 555 031</p>
    <p>pieter@stonebrookputt.co.ke</p>
    <p class="web">www.stonebrookputt.com</p>
  </div>

  <div class="partner-badge" role="img" aria-label="Partner association badge"></div>
</article>

<article class="business-card back" aria-label="Business card back">
  <svg class="card-swoosh" viewBox="0 0 525 300" preserveAspectRatio="none" aria-hidden="true">
    <defs>
      <linearGradient id="steelBack" x1="0" y1="0" x2="1" y2="1">
        <stop offset="0" stop-color="var(--steel-light)"/>
        <stop offset="1" stop-color="var(--steel-dark)"/>
      </linearGradient>
      <linearGradient id="redBack" x1="0" y1="0" x2="1" y2="0">
        <stop offset="0" stop-color="var(--brand-red)"/>
        <stop offset="1" stop-color="var(--brand-red-dark)"/>
      </linearGradient>
    </defs>
    <path d="M0 300 L0 215 C90 235 170 268 240 300 Z" fill="url(#steelBack)"/>
    <path d="M0 200 C100 220 190 258 270 300 L240 300 C170 268 90 235 0 215 Z" fill="url(#redBack)"/>
  </svg>

  <p class="wordmark">Stonebrook</p>
</article>

</body>
</html>
```